Wedding invitation - including print files

Details
45 invitations and envelopes required

Our names: Corin and Maribel

Wedding information
Venue
At the Thistlewood residence, 2847 Ferndale-Tarawhiti road, Clevedon, Auckland for both the ceremony and reception.

Date
Saturday 19th April 2025 (Easter weekend)

Timing
Ceremony is at 3pm

Transport
A bus will pick up at 1.30pm from Harbour Lantern Hotel
A bus will go back to town to at 11pm and 12.15am to Harbour Lantern Hotel with a stop through Clevedon for those staying closer to the venue.

Accomodation
A lot of airbnbs and hotels in clevedon if you wish to stay closer

Gifts
gifts aren’t necessary but a wishing well for a piece of art we will remember the day by.

Day After
We will be having some platters from 1pm on Sunday at (I will confirm this to you tomorrow sorry we are choosing between two places)

RSVP
By the 12th October 2024 to Corin 0274918265 corin@brookfieldgroup.co or Maribel 0275306194 maribel@lumastudio.co.nz

Here are concept ideas for the invitations and the aspects we like about them.
Three sided is practical to fit information

Font styles to use
Decorative

Colors

Designer to choose only greyscale colors for use in the design.

Requirements
Nice to have
• refer attachments and description
Should not have
• cant look cheap or tacky

```html
<!DOCTYPE html>
<html lang="en">
<head>
<meta charset="UTF-8">
<title>Corin &amp; Maribel — Wedding Welcome</title>
<link rel="stylesheet" href="https://fonts.googleapis.com/css2?family=Montserrat:wght@400;500;600&family=Mrs+Saint+Delafield&display=swap">
<style>
  :root {
    --paper: #e8e3df;
    --paper-shade: #c8c3c0;
    --ink-green: #30412d;
    --ink-script: #151214;
    --gold: #d9b48c;
    --bronze: #8f7a70;
    --ornament-gold: rgba(217, 180, 140, 0.22);
    --ornament-bronze: rgba(143, 122, 112, 0.24);
  }
  * { margin: 0; padding: 0; box-sizing: border-box; }
  html, body { width: 854px; height: 1200px; overflow: hidden; }
  body { background: var(--paper); }
  .welcome-sign {
    position: relative;
    width: 854px;
    height: 1200px;
    overflow: hidden;
    background: linear-gradient(90deg, var(--paper-shade) 0%, #dedad6 14%, var(--paper) 30%, var(--paper) 100%);
    font-family: "Montserrat", sans-serif;
    color: var(--ink-green);
  }
  .ornament {
    position: absolute;
    background: linear-gradient(90deg, var(--ornament-gold), var(--ornament-bronze) 50%, var(--ornament-gold));
  }
  .ornament--top {
    left: 155px; top: 16px; width: 538px; height: 155px;
    border-radius: 50% 50% 0 0 / 100% 100% 0 0;
  }
  .ornament--bottom {
    left: 281px; top: 1112px; width: 284px; height: 80px;
    border-radius: 0 0 50% 50% / 0 0 100% 100%;
  }
  .rule {
    position: absolute; left: 0; width: 854px; height: 1px;
    background: linear-gradient(90deg, rgba(217,180,140,0.4), var(--bronze) 50%, rgba(217,180,140,0.6));
  }
  .rule--top { top: 171px; }
  .rule--bottom-a { top: 1099px; height: 2px; }
  .rule--bottom-b { top: 1111px; opacity: 0.5; }
  .greeting {
    position: absolute; left: 0; width: 854px; top: 252px;
    text-align: center; font-weight: 500; font-size: 45px; line-height: 49px;
  }
  .couple {
    position: absolute; left: 0; width: 854px; top: 418px;
    text-align: center; color: var(--ink-script);
    font-family: "Mrs Saint Delafield", cursive;
  }
  .couple__name { display: block; font-size: 155px; line-height: 150px; }
  .couple__amp { display: block; font-size: 90px; line-height: 60px; margin: 6px 0 -4px 6px; }
  .date-block { position: absolute; left: 0; top: 0; width: 854px; height: 1200px; }
  .date-block__line {
    position: absolute; height: 3px; background: var(--ink-green); border-radius: 2px;
  }
  .date-block__line--upper { top: 860px; }
  .date-block__line--lower { top: 929px; }
  .date-block__line--left { left: 183px; width: 195px; }
  .date-block__line--right { left: 476px; width: 195px; }
  .date-block__text {
    position: absolute; font-weight: 500; line-height: 1; font-size: 32px; white-space: nowrap;
  }
  .date-block__month { left: 0; width: 854px; text-align: center; top: 822px; }
  .date-block__weekday { right: 471px; top: 879px; letter-spacing: -0.5px; }
  .date-block__day { left: 0; width: 854px; text-align: center; top: 846px; font-size: 98px; font-weight: 600; letter-spacing: -6px; text-indent: -6px; }
  .date-block__time { left: 529px; top: 879px; }
  .date-block__year { left: 0; width: 854px; text-align: center; top: 939px; }
</style>
</head>
<body>
  <main class="welcome-sign">
    <div class="ornament ornament--top" role="img" aria-label="Ornate scrollwork flourish in bronze and soft gold"></div>
    <div class="rule rule--top"></div>

    <h1 class="greeting">WELCOME<br>TO THE WEDDING OF</h1>

    <p class="couple">
      <span class="couple__name">Corin</span>
      <span class="couple__amp">&amp;</span>
      <span class="couple__name">Maribel</span>
    </p>

    <section class="date-block">
      <div class="date-block__line date-block__line--upper date-block__line--left"></div>
      <div class="date-block__line date-block__line--upper date-block__line--right"></div>
      <div class="date-block__line date-block__line--lower date-block__line--left"></div>
      <div class="date-block__line date-block__line--lower date-block__line--right"></div>
      <span class="date-block__text date-block__month">APRIL</span>
      <span class="date-block__text date-block__weekday">SATURDAY</span>
      <span class="date-block__text date-block__day">19</span>
      <span class="date-block__text date-block__time">3:00pm</span>
      <span class="date-block__text date-block__year">2025</span>
    </section>

    <div class="rule rule--bottom-a"></div>
    <div class="rule rule--bottom-b"></div>
    <div class="ornament ornament--bottom" role="img" aria-label="Small ornate scrollwork flourish in bronze and soft gold"></div>
  </main>
</body>
</html>
```